LVNODE
biz card
LVNODE - Information Technology
Creative Brief
Professional
jun pa
238 Elmora Pl, 3FL NewYorkCity, NY 10583
jun.pa@lanviretnode.com
www.lanviretnode.com

```html
<!DOCTYPE html>
<html lang="en">
<head>
<meta charset="utf-8">
<title>LVNODE business card</title>
<link rel="stylesheet" href="https://fonts.googleapis.com/css2?family=Arimo:wght@400;700&display=swap">
<style>
  :root {
    --bg: #ece9e4;
    --card-white: #ffffff;
    --red: #d3202f;
    --red-dark: #9e0f1c;
    --grey: #8c8c8c;
    --grey-dark: #4f4f4f;
    --swoosh-grey: #b9b9b9;
    --swoosh-red: #c51a28;
    --brand-red: #d3202f;
    --text-light: #ffffff;
  }
  html, body {
    margin: 0;
    padding: 0;
    width: 1200px;
    height: 410px;
    overflow: hidden;
    background: var(--bg);
    font-family: "Arimo", Arial, sans-serif;
  }
  .canvas {
    position: relative;
    width: 1200px;
    height: 410px;
  }
  .card {
    position: absolute;
    top: 40px;
    width: 570px;
    height: 330px;
    border-radius: 14px;
    overflow: hidden;
    background: var(--card-white);
    box-shadow: 0 3px 10px rgba(0,0,0,0.22);
  }
  .card--red { left: 36px; }
  .card--grey { left: 624px; }
  .card-art {
    position: absolute;
    inset: 0;
    width: 570px;
    height: 330px;
  }
  .brand {
    position: absolute;
    left: 46px;
    top: 118px;
    width: 150px;
    display: flex;
    flex-direction: column;
    align-items: center;
    gap: 12px;
  }
  .brand-mark {
    width: 46px;
    height: 46px;
    background: var(--brand-red);
  }
  .brand-name {
    font-weight: 700;
    font-size: 30px;
    letter-spacing: 1px;
    color: var(--brand-red);
    line-height: 1;
  }
  .holder-name {
    position: absolute;
    right: 30px;
    top: 24px;
    margin: 0;
    font-weight: 700;
    font-size: 21px;
    color: var(--text-light);
  }
  .contact {
    position: absolute;
    right: 30px;
    bottom: 22px;
    margin: 0;
    font-style: normal;
    text-align: right;
    font-size: 13px;
    line-height: 17.5px;
    color: var(--text-light);
  }
</style>
</head>
<body>
<main class="canvas">

  <article class="card card--red">
    <svg class="card-art" viewBox="0 0 570 330" aria-hidden="true">
      <defs>
        <radialGradient id="redPanel" cx="0.65" cy="0.45" r="0.7">
          <stop offset="0" stop-color="var(--red)"/>
          <stop offset="1" stop-color="var(--red-dark)"/>
        </radialGradient>
      </defs>
      <path d="M246 0 C176 90 262 210 176 330 L206 330 C286 210 206 90 272 0 Z" fill="var(--swoosh-grey)"/>
      <path d="M262 0 C196 92 282 212 198 330 L570 330 L570 0 Z" fill="url(#redPanel)"/>
    </svg>
    <div class="brand">
      <div class="brand-mark"></div>
      <div class="brand-name">LVNODE</div>
    </div>
    <h2 class="holder-name">Jun pa</h2>
    <address class="contact">
      238 Elmora Pl, 3FL<br>
      NewYorkCity, NY 10583<br>
      P: 212-555-0147<br>
      F: 212-555-0147<br>
      C: 212-555-0147<br>
      E: jun.pa@lanviretnode.com<br>
      www.lanviretnode.com
    </address>
  </article>

  <article class="card card--grey">
    <svg class="card-art" viewBox="0 0 570 330" aria-hidden="true">
      <defs>
        <radialGradient id="greyPanel" cx="0.65" cy="0.45" r="0.7">
          <stop offset="0" stop-color="var(--grey)"/>
          <stop offset="1" stop-color="var(--grey-dark)"/>
        </radialGradient>
      </defs>
      <path d="M246 0 C176 90 262 210 176 330 L206 330 C286 210 206 90 272 0 Z" fill="var(--swoosh-red)"/>
      <path d="M262 0 C196 92 282 212 198 330 L570 330 L570 0 Z" fill="url(#greyPanel)"/>
    </svg>
    <div class="brand">
      <div class="brand-mark"></div>
      <div class="brand-name">LVNODE</div>
    </div>
    <h2 class="holder-name">Jun pa</h2>
    <address class="contact">
      238 Elmora Pl, 3FL<br>
      NewYorkCity, NY 10583<br>
      P: 212-555-0147<br>
      F: 212-555-0147<br>
      C: 212-555-0147<br>
      E: jun.pa@lanviretnode.com<br>
      www.lanviretnode.com
    </address>
  </article>

</main>
</body>
</html>
```